依頼詳細
明るくポップなイメージでお願いします。
記載事項については添付データを参考にしてください。
イメージ画像も添付してありますが特にこだわりはありませんので、必要事項が入っていればどのようなデザインでも構いません。
年間通して使用するため季節感のないものでお願いします。
記載項目
添付データ参照
希望イメージ
シンプル 複雑
単色 カラフル
暗い 明るい
日常 高級
遊び心 厳粛
未来的 伝統的
女性的 男性的
希望する色
赤系、黄・オレンジ系、無彩色系
納品ファイル
設定なし
補足説明
プレゼントになる景品の画像をご用意いただきたいです。
データ納品後にこちらで差し替える可能性もございますが、そのまま使用する可能性もあるので使用しても問題ない画像を入れてください。
■ 選んだ理由

弊社の企業HPを調べていただいたのだと思いますが、弊社が取り扱っている製品をイラストアイコン化させて掲載されていたことがとても印象強く、社内でも驚きと感動の声があがりました。しっかりと背景を読み込んだうえでご制作いただいたのではないかと思うとお気遣いがとてもうれしく感じました。また、デザインも希望しているものに沿ったデザインで社内で一番好評でした。

■ 提案者全員のお礼・コメント

たくさんのご応募ありがとうございました。本当に素敵なデザインが多くすべての方を当選にしたくなるほど悩みました。裏面までデザインいただいた方もいらっしゃりとても感激いたしました。皆様たくさんのご応募ありがとうございました。

```html
<!DOCTYPE html>
<html lang="ja">
<head>
<meta charset="utf-8">
<title>プレゼントキャンペーン</title>
<link href="https://fonts.googleapis.com/css2?family=M+PLUS+Rounded+1c:wght@700;800&family=Noto+Sans+JP:wght@400;500;700;900&display=swap" rel="stylesheet">
<style>
  :root{
    --red:#e8514f;
    --red-deep:#d8393a;
    --title:#e8473f;
    --yellow:#ffe94a;
    --ink:#222;
    --muted:#555;
    --line:#e28a88;
    --sky:#cfe9f7;
    --sea:#4aa7dd;
    --brand:#3b6fb8;
    --white:#fff;
  }
  *{margin:0;padding:0;box-sizing:border-box}
  html,body{width:812px;height:1200px;overflow:hidden;background:var(--white)}
  body{font-family:"Noto Sans JP",sans-serif;color:var(--ink);position:relative}
  .flyer{position:absolute;inset:0;overflow:hidden;background:var(--white)}

  .brand{position:absolute;top:30px;right:22px;display:flex;align-items:center;gap:6px;
    font-family:"Noto Sans JP",sans-serif;font-weight:700;font-size:12px;color:var(--brand);letter-spacing:.03em}
  .brand-dot{width:12px;height:12px;border-radius:50%;background:var(--brand)}

  .title{position:absolute;top:24px;left:0;right:0;text-align:center;
    font-family:"M PLUS Rounded 1c","Noto Sans JP",sans-serif;font-weight:800;font-size:46px;line-height:1.2;
    color:var(--title);letter-spacing:.02em}
  .title-rule{position:absolute;top:88px;height:3px;background:var(--title);border-radius:2px}
  .title-rule.left{left:160px;width:110px}
  .title-rule.right{right:160px;width:110px}

  .intro{position:absolute;top:106px;left:40px;right:30px;font-size:18.5px;line-height:1.55;
    font-weight:500;white-space:nowrap}

  .splash{position:absolute;top:262px;left:0;right:0;height:200px;
    background:linear-gradient(180deg,var(--sky) 0%,#a9d8f2 45%,var(--sea) 100%)}

  .prize{position:absolute;top:282px;width:236px;height:236px;border-radius:50%;
    border:6px solid var(--white);box-shadow:0 4px 10px rgba(0,0,0,.15)}
  .prize.meat{left:28px;background:radial-gradient(circle at 45% 45%,#e7a0a0,#b8423c 70%,#7d2a26)}
  .prize.sea{left:288px;background:radial-gradient(circle at 50% 50%,#f07a3a,#c73a1d 65%,#7a2714)}
  .prize.sweets{left:548px;background:radial-gradient(circle at 50% 45%,#fbe7e8,#e24a4f 60%,#a82a2f)}

  .prize-label{position:absolute;top:264px;display:flex;align-items:center;gap:6px;
    font-family:"M PLUS Rounded 1c","Noto Sans JP",sans-serif;font-weight:800;font-size:30px;color:var(--white);
    text-shadow:0 0 4px rgba(0,0,0,.45)}
  .prize-label .badge{width:40px;height:40px;border-radius:50%;background:var(--red-deep);
    display:flex;align-items:center;justify-content:center;font-size:26px;text-shadow:none}
  .prize-label.a{left:52px}
  .prize-label.b{left:316px}
  .prize-label.c{left:574px}

  .entry{position:absolute;top:470px;left:0;right:0;height:610px;background:var(--red)}
  .gift-icon{position:absolute;top:44px;left:42px;width:80px;height:80px}
  .choose{position:absolute;top:40px;left:140px;font-size:27px;font-weight:700;color:var(--yellow);letter-spacing:.02em}
  .choice-row{position:absolute;top:88px;left:140px;display:flex;gap:58px;
    font-size:32px;font-weight:700;color:var(--yellow);letter-spacing:.06em}

  .form{position:absolute;top:150px;left:40px;right:40px;height:440px;background:var(--white)}
  .field{position:absolute;left:0;right:0;border-bottom:2px dotted var(--line);
    font-size:23px;font-weight:500;color:#333;padding-left:26px;display:flex;align-items:center}
  .field.name{top:0;height:80px}
  .field.phone{top:80px;height:80px}
  .field.address{top:160px;height:100px;align-items:flex-start;padding-top:24px}
  .field.address .zip{margin-left:132px}
  .comments{position:absolute;top:260px;left:0;right:0;bottom:0;padding:18px 26px}
  .comments p{font-size:17px;color:var(--muted)}
  .comments .rule{border-bottom:2px dotted var(--line);height:44px}

  .notes{position:absolute;top:1090px;left:26px;right:26px;font-size:12.5px;line-height:1.62;color:var(--ink)}
</style>
</head>
<body>
<main class="flyer">
  <div class="brand"><span class="brand-dot"></span>SUISUI WATER</div>

  <h1 class="title">プレゼントキャンペーン</h1>
  <span class="title-rule left"></span><span class="title-rule right"></span>

  <p class="intro">いつも弊社ウォーターサーバーをご使用いただき、誠にありがとうございます。<br>感謝の気持ちを込めて、プレゼントキャンペーンを開催いたします！<br>下記３つからお好きなプレゼントをお選びください。抽選で１名様ずつご希望の<br>プレゼントを進呈いたします。たくさんのご応募をお待ちしております♪</p>

  <div class="splash" role="img" aria-label="水しぶきの写真"></div>

  <div class="prize meat" role="img" aria-label="霜降り牛肉の写真"></div>
  <div class="prize sea" role="img" aria-label="カニやエビなど海鮮の写真"></div>
  <div class="prize sweets" role="img" aria-label="いちごのスイーツの写真"></div>

  <div class="prize-label a"><span class="badge">A</span>お肉</div>
  <div class="prize-label b"><span class="badge">B</span>海鮮</div>
  <div class="prize-label c"><span class="badge">C</span>スイーツ</div>

  <section class="entry">
    <svg class="gift-icon" viewBox="0 0 80 80" aria-hidden="true">
      <g fill="none" stroke="#fff" stroke-width="4" stroke-linejoin="round">
        <rect x="8" y="30" width="64" height="16"/>
        <rect x="13" y="46" width="54" height="28"/>
        <line x1="40" y1="30" x2="40" y2="74"/>
        <path d="M40 30 C30 14 16 16 20 26 C22 30 32 30 40 30 Z"/>
        <path d="M40 30 C50 14 64 16 60 26 C58 30 48 30 40 30 Z"/>
      </g>
    </svg>
    <p class="choose">ご希望のプレゼントに〇を付けてください</p>
    <div class="choice-row"><span>プレゼント</span><span>A</span><span>B</span><span>C</span></div>

    <div class="form">
      <div class="field name">お 名 前</div>
      <div class="field phone">お電話番号</div>
      <div class="field address">ご 住 所<span class="zip">〒</span></div>
      <div class="comments">
        <p>ご意見やご感想などありましたら、ぜひご記入ください。</p>
        <div class="rule"></div>
        <div class="rule"></div>
        <div class="rule"></div>
      </div>
    </div>
  </section>

  <p class="notes">[注意事項]●記入事項に不備がある場合は無効となります。●ご応募はお一人様一回までとさせていただきます。●ご応募いただいた個人情報は、当選のご連絡および賞品の発送にのみ使用いたします。●賞品の発送は日本国内に限らせていただきます。●当選者の発表は賞品の発送をもってかえさせていただきます。●賞品の内容は予告なく変更となる場合がございます。●賞品の換金・転売はご遠慮ください。●キャンペーン内容は都合により変更・終了となる場合がございます。●お問い合わせは弊社カスタマーセンターまでお願いいたします。</p>
</main>
</body>
</html>
```